Tulmex Business Card

I already have the conplay logo. I need to develop a professional business card layout

Target Market(s)

Business

Industry/Entity Type

Business

Contact Information for Business Card

Company Name: Tulmex Limited

Font styles to use
Sans Serif

Colors

Designer to choose colors to be used in the design.

Requirements
Must have
• Use current logo
• Need two card size options:
• Small Card: 70mm x 28mm (Landscape)
• Square Card: 65mm x 65mm
Nice to have
• I will need 8-10 files for each name, number and email address (details to follow)

```html
<!DOCTYPE html>
<html lang="en">
<head>
<meta charset="utf-8">
<title>Tulmex Limited – Business Cards</title>
<link rel="stylesheet" href="https://fonts.googleapis.com/css2?family=Fira+Sans:wght@400;600;700&display=swap">
<style>
  :root {
    --stage-light: #f1dede;
    --stage-mid: #d19a9a;
    --stage-dark: #9e2526;
    --card-white: #ffffff;
    --ink: #2b2b2b;
    --band-orange: #ee7f22;
    --band-red: #e32027;
    --band-green: #026b37;
    --band-dark: #2b2b2b;
    --brand: #026b37;
    --on-dark: #ffffff;
  }
  * { margin: 0; padding: 0; box-sizing: border-box; }
  html, body { width: 1200px; height: 977px; overflow: hidden; }
  body {
    position: relative;
    font-family: "Fira Sans", Arial, sans-serif;
    background: radial-gradient(ellipse 75% 75% at 50% 50%, var(--stage-light) 0%, var(--stage-mid) 55%, var(--stage-dark) 100%);
  }
  .card {
    position: absolute;
    background: var(--card-white);
    box-shadow: 6px 8px 9px rgba(0,0,0,0.35);
    overflow: hidden;
  }
  .card--square { left: 56px; top: 117px; width: 690px; height: 689px; }
  .card--slim { left: 798px; top: 91px; width: 297px; height: 742px; }
  .card__bands { position: absolute; left: 0; top: 0; width: 100%; height: 100%; display: block; }
  .card__line {
    position: absolute; left: 0; width: 100%;
    text-align: center; line-height: 1; white-space: nowrap;
    transform: translateY(-50%);
  }
  .brand-name { color: var(--brand); font-weight: 700; letter-spacing: 0.02em; }
  .person-name { color: var(--ink); font-weight: 700; }
  .person-role { color: var(--ink); font-weight: 400; }
  .contact { color: var(--on-dark); font-weight: 400; z-index: 1; }

  .card--square .brand-name { top: 142px; font-size: 92px; }
  .card--square .person-name { top: 298px; font-size: 55px; }
  .card--square .person-role { top: 354px; font-size: 43px; }
  .card--square .contact { font-size: 27px; }
  .card--square .contact--tel { top: 551px; }
  .card--square .contact--email { top: 600px; }
  .card--square .contact--social { top: 649px; }

  .card--slim .person-name { top: 122px; font-size: 36px; }
  .card--slim .person-role { top: 164px; font-size: 30px; }
  .card--slim .brand-name { top: 329px; font-size: 46px; }
  .card--slim .contact { font-size: 29px; }
  .card--slim .contact--email { top: 645px; }
  .card--slim .contact--tel { top: 679px; }
</style>
</head>
<body>

<section class="card card--square" aria-label="Square business card">
  <svg class="card__bands" viewBox="0 0 767 766" preserveAspectRatio="none" aria-hidden="true">
    <polygon fill="var(--band-orange)" points="0,448 555,520 0,478"/>
    <polygon fill="var(--band-red)" points="0,478 555,520 0,600"/>
    <polygon fill="var(--band-green)" points="555,520 767,481 767,556"/>
    <polygon fill="var(--band-dark)" points="0,600 555,520 767,556 767,766 0,766"/>
  </svg>
  <div class="card__line brand-name">TULMEX</div>
  <div class="card__line person-name">R.M. HALE</div>
  <div class="card__line person-role">Fine Artist</div>
  <div class="card__line contact contact--tel">Tel: 07946 318 207</div>
  <div class="card__line contact contact--email">Email: rmhale@studiomail.com</div>
  <div class="card__line contact contact--social">Twitter: @rmhalepaints</div>
</section>

<section class="card card--slim" aria-label="Slim business card">
  <svg class="card__bands" viewBox="0 0 330 825" preserveAspectRatio="none" aria-hidden="true">
    <polygon fill="var(--band-orange)" points="0,548 231,606 0,572"/>
    <polygon fill="var(--band-red)" points="0,572 231,606 0,671"/>
    <polygon fill="var(--band-green)" points="231,606 330,571 330,639"/>
    <polygon fill="var(--band-dark)" points="0,671 231,606 330,639 330,825 0,825"/>
  </svg>
  <div class="card__line person-name">ARJUN MEHRA</div>
  <div class="card__line person-role">Fashion Designer</div>
  <div class="card__line brand-name">TULMEX</div>
  <div class="card__line contact contact--email">hi@arjunmehra.com</div>
  <div class="card__line contact contact--tel">301 555 2741</div>
</section>

</body>
</html>
```